Face Mask Box

We need a box design for medical face masks, with our brand logo and emphasizing that the product is made in the USA, so maybe more than just a made in USA icon maybe the packaging should be red/white/blue or a flag etc... would like an image of the product (which we can substitute later) or the product being worn, maybe a rendering as well. Icons for all of its features (we can put those on later), a place for the UPC. We can put text on later, looking for the base graphic design right now.

```html
<!DOCTYPE html>
<html lang="en">
<head>
<meta charset="utf-8">
<title>Veloura Disposable Medical Mask Box</title>
<link href="https://fonts.googleapis.com/css2?family=Montserrat:wght@500;700;800&family=Roboto+Condensed:wght@400;700&display=swap" rel="stylesheet">
<style>
  :root {
    --page-bg: #ececec;
    --panel-white: #f7f8f9;
    --orange: #e9b04a;
    --orange-deep: #dc9a2c;
    --blue: #5aaee4;
    --blue-deep: #3f8fd1;
    --blue-light: #8ccaf0;
    --navy: #2b3a6b;
    --grey-text: #a6a8ab;
    --grey-panel: #e4e5e7;
    --ink: #2a2a2a;
    --white: #ffffff;
  }
  * { margin: 0; padding: 0; box-sizing: border-box; }
  html, body { width: 1200px; height: 1200px; overflow: hidden; }
  body {
    background: radial-gradient(ellipse at 50% 45%, #f6f6f6 0%, var(--page-bg) 75%);
    font-family: "Montserrat", sans-serif;
    position: relative;
  }
  .box-front {
    position: absolute;
    left: 50px; top: 347px;
    width: 1100px; height: 506px;
    background: var(--panel-white);
    overflow: hidden;
  }
  .count-badge {
    position: absolute;
    left: 57px; top: 39px;
    width: 138px; height: 138px;
    border-radius: 50%;
    border: 6px solid var(--orange);
    background: radial-gradient(circle at 40% 35%, var(--blue-light) 0%, var(--blue) 55%, var(--blue-deep) 100%);
    color: var(--white);
    text-align: center;
    z-index: 2;
  }
  .count-badge .count-number {
    display: block;
    font-weight: 800;
    font-size: 64px;
    line-height: 1;
    margin-top: 20px;
  }
  .count-badge .count-unit {
    display: block;
    font-weight: 500;
    font-size: 18px;
    letter-spacing: 0.5px;
    margin-top: 2px;
  }
  .ply-tag {
    position: absolute;
    left: 180px; top: 79px;
    width: 142px; height: 64px;
    background: var(--orange);
    border-radius: 0 6px 6px 0;
    color: var(--white);
    font-family: "Roboto Condensed", sans-serif;
    font-size: 38px;
    line-height: 64px;
    padding-left: 30px;
  }
  .brand-name {
    position: absolute;
    left: 410px; top: 137px;
    display: flex; align-items: center; gap: 12px;
  }
  .brand-name .brand-dot {
    width: 18px; height: 18px; border-radius: 50%;
    background: var(--orange);
  }
  .brand-name .brand-word {
    font-family: "Montserrat", sans-serif;
    font-weight: 500;
    font-size: 36px;
    color: var(--ink);
    letter-spacing: 0.5px;
  }
  .origin-mark {
    position: absolute;
    left: 950px; top: 41px;
    width: 90px;
    text-align: center;
  }
  .origin-mark .flag-art { display: block; width: 84px; height: 44px; margin: 0 auto; }
  .origin-mark .origin-label {
    display: block;
    margin-top: 4px;
    font-family: "Roboto Condensed", sans-serif;
    font-weight: 700;
    font-size: 15px;
    color: var(--navy);
  }
  .title-band {
    position: absolute;
    left: 0; top: 219px;
    width: 700px; height: 72px;
    background: var(--orange);
    color: var(--white);
    font-weight: 700;
    font-size: 35px;
    line-height: 72px;
    padding-left: 60px;
    letter-spacing: 0.3px;
  }
  .feature-band {
    position: absolute;
    left: 0; top: 291px;
    width: 1100px; height: 185px;
    background: linear-gradient(90deg, var(--blue-light) 0%, var(--blue) 45%, var(--blue-deep) 100%);
  }
  .bfe-panel {
    position: absolute;
    left: 0; top: 310px;
    width: 232px; height: 166px;
    background: linear-gradient(90deg, #f2f3f4 0%, var(--grey-panel) 100%);
    border-radius: 0 14px 0 0;
    color: var(--grey-text);
  }
  .bfe-panel .bfe-value {
    position: absolute;
    left: 60px; top: 18px;
    font-weight: 500;
    font-size: 68px;
    line-height: 1;
  }
  .bfe-panel .bfe-label {
    position: absolute;
    left: 62px; top: 92px;
    font-family: "Roboto Condensed", sans-serif;
    font-weight: 700;
    font-size: 48px;
    line-height: 1;
  }
  .bfe-panel .bfe-note {
    position: absolute;
    left: 146px; top: 94px;
    width: 62px;
    font-family: "Roboto Condensed", sans-serif;
    font-size: 8.5px;
    line-height: 1.35;
    text-transform: uppercase;
    border-left: 1px solid var(--grey-text);
    border-right: 1px solid var(--grey-text);
    padding: 2px 3px;
  }
  .feature-list {
    position: absolute;
    left: 250px; top: 322px;
    list-style: none;
    color: var(--white);
    font-family: "Roboto Condensed", sans-serif;
    font-size: 22px;
    line-height: 34px;
    text-transform: uppercase;
  }
  .feature-list li::before { content: "+ "; }
  .product-art {
    position: absolute;
    left: 690px; top: 110px;
    width: 400px; height: 240px;
  }
  .bottom-strip {
    position: absolute;
    left: 0; top: 476px;
    width: 1100px; height: 30px;
    background: var(--panel-white);
  }
</style>
</head>
<body>
  <main class="box-front">
    <div class="feature-band"></div>

    <div class="ply-tag">3 PLY</div>
    <div class="count-badge">
      <span class="count-number">50</span>
      <span class="count-unit">PIECES</span>
    </div>

    <div class="brand-name">
      <span class="brand-dot"></span>
      <span class="brand-word">VELOURA</span>
    </div>

    <div class="origin-mark">
      <svg class="flag-art" viewBox="0 0 84 44" role="img" aria-label="United States flag">
        <defs>
          <linearGradient id="flagTone" x1="0" y1="0" x2="1" y2="1">
            <stop offset="0" stop-color="#3b4f8f"/>
            <stop offset="0.45" stop-color="#c9404a"/>
            <stop offset="1" stop-color="#e8d6d8"/>
          </linearGradient>
        </defs>
        <rect width="84" height="44" fill="url(#flagTone)"/>
      </svg>
      <span class="origin-label">Made in USA</span>
    </div>

    <div class="title-band">DISPOSABLE MEDICAL MASK</div>

    <div class="bfe-panel">
      <span class="bfe-value">98%</span>
      <span class="bfe-label">BFE</span>
      <span class="bfe-note">Bacterial Filtration Efficiency</span>
    </div>

    <ul class="feature-list">
      <li>Easy to breath</li>
      <li>Elastic ear loops</li>
      <li>Adjustable nosepiece</li>
      <li>Soft and comfortable material</li>
    </ul>

    <svg class="product-art" viewBox="0 0 400 240" role="img" aria-label="Product photo of a blue pleated disposable face mask with white ear loop">
      <defs>
        <radialGradient id="maskTone" cx="0.4" cy="0.45" r="0.7">
          <stop offset="0" stop-color="#d9effb"/>
          <stop offset="0.6" stop-color="#8fcdf0"/>
          <stop offset="1" stop-color="#6bb8e6"/>
        </radialGradient>
      </defs>
      <rect width="400" height="240" rx="40" fill="url(#maskTone)"/>
    </svg>

    <div class="bottom-strip"></div>
  </main>
</body>
</html>
```